Start a weight loss Clinic

build a landing page website using the content from this websites. we want to copy all the content from slimpathcoaching.net but make page look more professional. we dont have a logo yet but url is www.brightvitalitycentre.com
https://clinicwellnessalliancegroup.net/home-page
https://www.slimpathcoaching.net/

Target Market(s)

people looking to open a weightloss clinic or a franchise opportunity

Coding

Number of Pages Required

3 page

Requirements
Must have
• copy all content from other site https://www.slimpathcoaching.net/

```html
<!DOCTYPE html>
<html lang="en">
<head>
<meta charset="utf-8">
<title>Bright Vitality — Start Your Own Weight Loss Clinic</title>
<link href="https://fonts.googleapis.com/css2?family=Cinzel:wght@600;700&family=Open+Sans:wght@400;600;700;800&display=swap" rel="stylesheet">
<style>
:root{
  --navy:#0c3878;
  --navy-deep:#072856;
  --red:#d8232c;
  --red-dark:#a8141b;
  --grey:#eeeff1;
  --grey-mid:#d9dbdf;
  --ink:#3a3f48;
  --white:#ffffff;
  --display:'Cinzel', Georgia, serif;
  --body:'Open Sans', Arial, sans-serif;
}
*{box-sizing:border-box;margin:0;padding:0}
html,body{width:1200px;height:3096px;overflow:hidden}
body{font-family:var(--body);color:var(--ink);background:var(--white);position:relative}
section,header,footer{position:absolute;left:0;width:1200px}
.ph{position:absolute}
.btn{display:inline-block;background:var(--red);color:var(--white);font:700 12px/1 var(--body);letter-spacing:1px;text-transform:uppercase;padding:15px 30px;border-radius:3px}
.brand{display:flex;align-items:center;gap:10px;color:var(--white);font:800 20px/1 var(--body)}
.brand-dot{width:30px;height:30px;border-radius:50%;background:var(--red)}

/* hero */
.hero{top:0;height:520px;background:linear-gradient(90deg,var(--navy-deep) 0%,var(--navy) 45%,#2d5da3 100%);overflow:hidden}
.hero-photo{right:0;top:0;width:640px;height:500px;background:linear-gradient(120deg,#a9c3e2 0%,#e9eef5 55%,#c9d6e8 100%)}
.hero-fade{position:absolute;left:560px;top:0;width:160px;height:500px;background:linear-gradient(90deg,var(--navy) 0%,rgba(12,56,120,0) 100%)}
.hero-swoosh{position:absolute;left:0;bottom:0}
.nav{position:absolute;top:0;left:0;width:1200px;height:72px;display:flex;align-items:center;padding:0 60px}
.nav ul{list-style:none;display:flex;gap:26px;margin-left:140px}
.nav li{color:var(--white);font:600 11px/1 var(--body);letter-spacing:.8px;text-transform:uppercase}
.nav li.active{border-bottom:2px solid var(--red);padding-bottom:6px}
.hero-copy{position:absolute;left:60px;top:120px;width:470px;color:var(--white)}
.hero-copy h1{font:700 42px/1.18 var(--display);text-transform:uppercase}
.hero-copy p{font:400 12.5px/1.7 var(--body);margin:20px 0 28px;opacity:.9}

/* about */
.about{top:520px;height:420px;background:var(--grey)}
.about-photo{left:60px;top:20px;width:280px;height:390px;background:linear-gradient(180deg,#c9ccd2,#f3f3f5)}
.about-mark{position:absolute;left:250px;top:110px;width:190px;height:190px;border-radius:50%;background:var(--white);border:6px solid var(--navy);display:flex;align-items:center;justify-content:center;text-align:center;font:800 18px/1.2 var(--body);color:var(--navy)}
.about-copy{position:absolute;left:590px;top:60px;width:540px}
.about-copy h2{font:700 36px/1 var(--display);color:var(--navy);text-transform:uppercase;margin-bottom:18px}
.about-copy p{font:400 12px/1.75 var(--body);margin-bottom:14px}

/* offer */
.offer{top:940px;height:720px;background:var(--white);overflow:hidden}
.offer-head{position:absolute;left:0;top:55px;width:1200px;text-align:center}
.offer-head h2{font:700 38px/1 var(--display);color:var(--navy);text-transform:uppercase}
.offer-head h3{font:700 20px/1 var(--body);color:var(--ink);margin:14px 0 18px}
.offer-head p{width:860px;margin:0 auto;font:400 12px/1.75 var(--body)}
.offer-photo{right:0;top:250px;width:230px;height:440px;background:linear-gradient(180deg,#f1dcd0,#ffffff)}
.cards{position:absolute;left:120px;top:300px;display:flex;gap:28px}
.card{width:200px;height:240px;border-radius:8px;background:var(--grey-mid);display:flex;flex-direction:column;align-items:center;justify-content:center;text-align:center;padding:20px;box-shadow:0 6px 14px rgba(0,0,0,.1)}
.card-icon{width:70px;height:70px;border-radius:50%;border:3px solid var(--red);display:flex;align-items:center;justify-content:center;margin-bottom:20px}
.card h4{font:700 16px/1.3 var(--body);color:var(--ink)}
.card.is-active{background:linear-gradient(160deg,var(--red) 0%,var(--navy) 60%)}
.card.is-active h4{color:var(--white)}
.card.is-active .card-icon{border-color:var(--white)}
.offer .btn{position:absolute;left:540px;top:590px}

/* benefits band */
.benefits{top:1660px;height:400px}
.benefits svg{position:absolute;left:0;top:0}
.benefits-copy{position:absolute;left:120px;top:70px;color:var(--white)}
.benefits-copy h2{font:700 36px/1 var(--display);text-transform:uppercase;margin-bottom:30px}
.checklist{display:grid;grid-template-columns:260px 260px;row-gap:14px;list-style:none}
.checklist li{display:flex;align-items:center;gap:10px;font:600 13px/1 var(--body)}
.btn-outline{display:inline-block;margin-top:34px;border:2px solid var(--white);color:var(--white);font:700 12px/1 var(--body);letter-spacing:1px;padding:13px 26px;border-radius:3px;text-transform:uppercase}
.benefits-photo{left:720px;top:40px;width:480px;height:300px;background:linear-gradient(90deg,rgba(216,35,44,0),rgba(255,210,200,.35))}

/* get started */
.start{top:2040px;height:360px}
.start h2{position:absolute;top:30px;width:1200px;text-align:center;font:700 36px/1 var(--display);color:var(--navy);text-transform:uppercase}
.steps{position:absolute;left:120px;top:95px;display:flex;gap:30px}
.step{width:300px;background:var(--white);box-shadow:0 6px 16px rgba(0,0,0,.12);border-radius:6px;overflow:hidden}
.step-photo{height:150px;background:linear-gradient(135deg,#c7d5e8,#eef2f7)}
.step-body{background:var(--navy);color:var(--white);text-align:center;padding:18px 22px 20px}
.step-body h4{font:700 19px/1 var(--body);margin-bottom:10px}
.step-body p{font:400 11px/1.6 var(--body);opacity:.9}

/* newsletter */
.learn{top:2400px;height:410px;overflow:hidden}
.learn-word{position:absolute;left:0;top:300px;width:1200px;text-align:center;font:800 86px/1 var(--body);color:#eceef1;letter-spacing:2px;text-transform:uppercase;white-space:nowrap}
.learn-photo{left:60px;top:10px;width:290px;height:400px;background:linear-gradient(180deg,#dde5f0,#b7c6dc)}
.learn h2{position:absolute;left:380px;top:40px;width:740px;text-align:center;font:700 34px/1 var(--display);color:var(--navy);text-transform:uppercase}
.signup{position:absolute;left:400px;top:110px;width:700px;height:76px;background:var(--navy);border-radius:4px;display:flex;align-items:center;padding:0 18px;gap:14px}
.signup .field{flex:1;height:44px;background:var(--white);border-radius:3px;display:flex;align-items:center;padding-left:16px;font:600 11px/1 var(--body);color:#8b919a;letter-spacing:.6px;text-transform:uppercase}

/* partners */
.partners{top:2810px;height:140px;background:var(--white);display:flex;align-items:center;justify-content:space-between;padding:0 100px}
.badge-round{width:70px;height:90px;border-radius:8px;background:var(--navy)}
.badge-society{width:200px;height:70px;border-radius:8px;background:#7a3f8e}
.badge-rect{width:110px;height:70px;border:3px solid var(--navy);border-radius:4px}

/* footer */
.footer{top:2950px;height:146px;background:var(--navy);color:var(--white);padding:22px 60px 0;display:flex;gap:110px}
.footer h5{font:700 13px/1 var(--body);letter-spacing:1px;margin-bottom:8px;text-transform:uppercase}
.footer ul{list-style:none}
.footer li{font:400 11px/1.6 var(--body);opacity:.9}
.footer .copy{font:400 10px/1 var(--body);opacity:.7;margin-top:24px}
.contact li{display:flex;align-items:center;gap:8px}
</style>
</head>
<body>

<header class="hero">
  <div class="ph hero-photo" role="img" aria-label="Photo of a coach taking a client's measurements in a bright clinic"></div>
  <div class="hero-fade"></div>
  <svg class="hero-swoosh" width="1200" height="140" viewBox="0 0 1200 140" aria-hidden="true">
    <path d="M0 140 L0 110 C300 150 700 120 1200 0 L1200 140 Z" fill="#ffffff"/>
    <path d="M0 112 C320 148 720 110 1200 0 L1200 22 C720 128 320 162 0 130 Z" fill="#d8232c"/>
  </svg>
  <nav class="nav">
    <div class="brand"><span class="brand-dot"></span>Bright Vitality</div>
    <ul>
      <li>Home</li><li class="active">About Us</li><li>What We Offer</li><li>Contact</li><li>FAQ</li><li>Contact Us</li>
    </ul>
  </nav>
  <div class="hero-copy">
    <h1>Start Your Own Profitable Weight Loss Clinic!</h1>
    <p>We are not a weight loss franchise — you are simply buying our business model, training and support for one low fee. Please read about us, look at what we offer and compare us to other franchises in the market. We offer you a proven program and simple steps to launch your clinic.</p>
    <span class="btn">Request a Free Market Analysis</span>
  </div>
</header>

<section class="about">
  <div class="ph about-photo" role="img" aria-label="Photo of a smiling woman holding a measuring tape"></div>
  <div class="about-mark">Bright<br>Vitality</div>
  <div class="about-copy">
    <h2>About Us</h2>
    <p>At Bright Vitality we have been operating clinics and training new owners for many years. We have developed a program that helps doctors, nurses and entrepreneurs open their own profitable weight loss centers with full guidance from day one.</p>
    <p>Our programs combine proven diet plans, patient protocols, marketing systems and hands-on training. Whether you want one location or several, we give you every tool to launch and grow a thriving clinic in your community.</p>
    <span class="btn">Learn More</span>
  </div>
</section>

<section class="offer">
  <div class="offer-head">
    <h2>Start Your Own</h2>
    <h3>Weight Loss &amp; Wellness Center</h3>
    <p>Bright Vitality offers you the tools and training you need to open and run your own successful weight loss and wellness center. We are not a franchise — you keep your profits, your name and your freedom. Compare our program to others and see why owners across the country choose us to build their clinics.</p>
  </div>
  <div class="ph offer-photo" role="img" aria-label="Photo of a woman holding a bowl of fresh salad"></div>
  <div class="cards">
    <div class="card is-active">
      <div class="card-icon"><svg width="34" height="34" viewBox="0 0 24 24" fill="none" stroke="#fff" stroke-width="2"><circle cx="8" cy="8" r="3"/><circle cx="16" cy="8" r="3"/><path d="M2 20c0-4 3-6 6-6s6 2 6 6M12 20c0-4 2-6 4-6s6 2 6 6"/></svg></div>
      <h4>One-on-one business &amp; medical training</h4>
    </div>
    <div class="card">
      <div class="card-icon"><svg width="34" height="34" viewBox="0 0 24 24" fill="none" stroke="#d8232c" stroke-width="2"><path d="M3 10v4h3l6 4V6L6 10z"/><path d="M16 9c1.5 1.5 1.5 4.5 0 6"/></svg></div>
      <h4>Marketing &amp; Advertising Training</h4>
    </div>
    <div class="card">
      <div class="card-icon"><svg width="34" height="34" viewBox="0 0 24 24" fill="none" stroke="#d8232c" stroke-width="2"><rect x="5" y="3" width="14" height="18" rx="2"/><path d="M9 8h6M9 12h6M9 16h4"/></svg></div>
      <h4>Diets, Patient Protocols &amp; Programs</h4>
    </div>
    <div class="card">
      <div class="card-icon"><svg width="34" height="34" viewBox="0 0 24 24" fill="none" stroke="#d8232c" stroke-width="2"><path d="M4 5h7v15H4zM13 5h7v15h-7z"/></svg></div>
      <h4>Office &amp; Operations Manuals</h4>
    </div>
  </div>
  <span class="btn">Read More</span>
</section>

<section class="benefits">
  <svg width="1200" height="400" viewBox="0 0 1200 400" aria-hidden="true">
    <path d="M0 40 C400 0 800 70 1200 20 L1200 370 C800 400 400 340 0 380 Z" fill="#d8232c"/>
    <path d="M0 40 C400 0 800 70 1200 20 L1200 40 C800 90 400 20 0 60 Z" fill="#a8141b"/>
  </svg>
  <div class="ph benefits-photo" role="img" aria-label="Soft photo of fresh vegetables and fruit"></div>
  <div class="benefits-copy">
    <h2>Start Your Own</h2>
    <ul class="checklist">
      <li><svg width="16" height="16" viewBox="0 0 16 16"><path d="M2 8l4 4 8-9" fill="none" stroke="#fff" stroke-width="2.4"/></svg>No franchise fees</li>
      <li><svg width="16" height="16" viewBox="0 0 16 16"><path d="M2 8l4 4 8-9" fill="none" stroke="#fff" stroke-width="2.4"/></svg>No monthly royalty fees</li>
      <li><svg width="16" height="16" viewBox="0 0 16 16"><path d="M2 8l4 4 8-9" fill="none" stroke="#fff" stroke-width="2.4"/></svg>No contracts</li>
      <li><svg width="16" height="16" viewBox="0 0 16 16"><path d="M2 8l4 4 8-9" fill="none" stroke="#fff" stroke-width="2.4"/></svg>No territory limits</li>
      <li><svg width="16" height="16" viewBox="0 0 16 16"><path d="M2 8l4 4 8-9" fill="none" stroke="#fff" stroke-width="2.4"/></svg>Use your own name</li>
      <li><svg width="16" height="16" viewBox="0 0 16 16"><path d="M2 8l4 4 8-9" fill="none" stroke="#fff" stroke-width="2.4"/></svg>You keep all profits</li>
      <li><svg width="16" height="16" viewBox="0 0 16 16"><path d="M2 8l4 4 8-9" fill="none" stroke="#fff" stroke-width="2.4"/></svg>Full training included</li>
      <li><svg width="16" height="16" viewBox="0 0 16 16"><path d="M2 8l4 4 8-9" fill="none" stroke="#fff" stroke-width="2.4"/></svg>Ongoing support</li>
    </ul>
    <span class="btn-outline">Contact Now</span>
  </div>
</section>

<section class="start">
  <h2>Get Started Today</h2>
  <div class="steps">
    <div class="step">
      <div class="step-photo" role="img" aria-label="Photo of a friendly receptionist on the phone"></div>
      <div class="step-body"><h4>Contact Us</h4><p>Call or email us to learn how you can open your own clinic.</p></div>
    </div>
    <div class="step">
      <div class="step-photo" role="img" aria-label="Photo of a doctor meeting a visitor in a clinic"></div>
      <div class="step-body"><h4>Visit Us</h4><p>Schedule a visit to one of our clinics and see our system in action.</p></div>
    </div>
    <div class="step">
      <div class="step-photo" role="img" aria-label="Photo of a bathroom scale and measuring tape"></div>
      <div class="step-body"><h4>Schedule a Webinar</h4><p>Join a live online session and ask our team your questions.</p></div>
    </div>
  </div>
</section>

<section class="learn">
  <div class="learn-word">Weight Loss Clinic</div>
  <div class="ph learn-photo" role="img" aria-label="Photo of a happy woman standing on a scale with arms raised"></div>
  <h2>Today to Learn More</h2>
  <div class="signup">
    <div class="field">Enter your email</div>
    <span class="btn">Subscribe</span>
  </div>
</section>

<section class="partners">
  <div class="badge-round" role="img" aria-label="Business accreditation badge"></div>
  <div class="badge-society" role="img" aria-label="Professional society membership badge"></div>
  <div class="badge-rect" role="img" aria-label="Medical association badge"></div>
</section>

<footer class="footer">
  <div>
    <div class="brand"><span class="brand-dot"></span>Bright Vitality</div>
    <p class="copy">© 2024 Bright Vitality. All rights reserved.</p>
  </div>
  <div>
    <h5>About Us</h5>
    <ul><li>Home</li><li>About Us</li><li>What We Offer</li><li>Contact</li><li>FAQ</li></ul>
  </div>
  <div class="contact">
    <h5>Contact Us</h5>
    <ul>
      <li><svg width="12" height="12" viewBox="0 0 24 24" fill="#fff"><path d="M12 2a7 7 0 0 0-7 7c0 5 7 13 7 13s7-8 7-13a7 7 0 0 0-7-7zm0 9.5A2.5 2.5 0 1 1 12 6a2.5 2.5 0 0 1 0 5.5z"/></svg>1420 Lindenway Court, Suite 210</li>
      <li><svg width="12" height="12" viewBox="0 0 24 24" fill="#fff"><path d="M6.6 10.8a15 15 0 0 0 6.6 6.6l2.2-2.2a1 1 0 0 1 1-.25 11.4 11.4 0 0 0 3.6.57 1 1 0 0 1 1 1V20a1 1 0 0 1-1 1A17 17 0 0 1 3 4a1 1 0 0 1 1-1h3.5a1 1 0 0 1 1 1c0 1.25.2 2.450.57 3.6a1 1 0 0 1-.25 1z"/></svg>(555) 014-2277</li>
      <li><svg width="12" height="12" viewBox="0 0 24 24" fill="none" stroke="#fff" stroke-width="2"><rect x="3" y="5" width="18" height="14"/><path d="M3 6l9 7 9-7"/></svg>info@vitalitystartdesk.org</li>
    </ul>
  </div>
</footer>

</body>
</html>
```